Broschüre
Zielgruppe
Wir sind eine ambulanter Pflegedienst in Rostock. Ab dem Herbst 25 bieten wir für Interessenten mit einem Pflegegrad begleitete reisen an. Eine Fachkraft wird Patienten mit Pflegegrad in kleinen Gruppen begleiten. Den Text für den Flyer haben wir eingefügt. Bitte die Bider aus dem Stock Portal wählen. Über den Flyer sollen Patienten gefunden werden.
Der Flyer
sollte Serios wirken und Reiselust der Senioren wecken.
Aufgabenstellung
Hier der Text für den Flyer:
Was wir bieten:
✔️ Begleitung durch erfahrene Pflegefachkräfte ✔️ Körperpflege, Medikamentengabe & Betreuung wie zuhause ✔️ 24-Stunden-Erreichbarkeit unserer Pflegekräfte vor Ort im gebuchten Hotel ✔️ Zusammenarbeit mit ausgewählten Hotels – barrierefrei & seniorengerecht ✔️ Kleine Gruppen & individuelle Betreuung vor Ort
Gut zu wissen:
Für unsere pflegerische Begleitung entstehen Ihnen keine zusätzlichen Kosten, wenn Sie einen Pflegegrad haben und das Verhinderungspflege-Budget noch nicht aufgebraucht ist.
Lediglich die Hotelkosten sind von Ihnen selbst zu tragen.
Wer hat Anspruch auf Verhinderungspflege?
Alle Pflegebedürftigen mit einem anerkannten Pflegegrad ab Stufe 2 können jährlich Verhinderungspflege über die Pflegekasse abrufen – ideal, um sich im Urlaub sicher begleiten zu lassen!
Unser Service – Ihr Mehrwert:
Wir organisieren Ihre Reise von A bis Z und begleiten Sie oder Ihre Angehörigen auf dem Weg zu Erholung und neuen Eindrücken – mit Herz, Kompetenz und Erfahrung. Vor Ort sind müssen Sie auf nichts verzichten und werden versorgt wie zu Hause. Gerne organisieren wir auch die Abholung aus ihrer Hässlichkeit.
???? Sonnenweg Touren – Ihr verlässlicher Partner für Pflege und Lebensfreude
???? Jetzt informieren & Platz sichern: 0381 - 72946183
???? Mail@sonnenweg-touren .de
???? www.sonnenweg-touren.de

```html
<!DOCTYPE html>
<html lang="de">
<head>
<meta charset="utf-8">
<title>Urlaub mit Pflege – Flyer</title>
<link href="https://fonts.googleapis.com/css2?family=Manrope:wght@400;500;700;800&display=swap" rel="stylesheet">
<style>
  :root{
    --navy:#1f2545;
    --orange:#e8782c;
    --paper:#ffffff;
    --mist:#f4f4f6;
    --ink:#1f2545;
    --stage:#ffffff;
  }
  *{margin:0;padding:0;box-sizing:border-box}
  html,body{width:1200px;height:960px;overflow:hidden;background:var(--stage);font-family:"Manrope",sans-serif;color:var(--ink)}
  .page{position:absolute;top:151px;width:465px;height:656px;overflow:hidden;background:var(--paper);z-index:0}
  .page--front{left:98px}
  .page--back{left:634px;background:var(--mist)}
  .page svg.art{position:absolute;left:0;top:0}
  .headline{position:absolute;left:172px;width:270px;text-align:center;color:#fff;font-weight:700;line-height:1}
  .headline__main{top:378px;font-size:33px}
  .headline__accent{top:416px;font-size:33px;color:var(--orange)}
  .headline__rule{position:absolute;left:281px;top:467px;width:33px;height:3px;background:#fff}
  .headline__sub{top:485px;font-size:23px;line-height:27px}
  .badge{position:absolute;left:366px;top:336px;width:80px;height:80px;border-radius:50%;background:var(--orange);color:var(--navy);font-weight:800;font-size:13.5px;line-height:17px;text-align:center;padding-top:15px}
  .badge span{color:#fff}
  .footer{position:absolute;left:0;top:600px;width:465px;height:36px}
  .brand{position:absolute;left:36px;top:0;display:flex;align-items:center;gap:9px}
  .brand__dot{width:36px;height:36px;border-radius:50%;background:var(--navy)}
  .brand__name{font-size:17px;font-weight:800;color:var(--navy);white-space:nowrap}
  .footer__url{position:absolute;left:267px;top:10px;font-size:11.5px;font-weight:500;color:var(--navy)}
  .content{position:absolute;left:40px;top:40px;width:385px;letter-spacing:-0.15px}
  .content h2{font-size:14.5px;font-weight:800;line-height:16px;color:var(--navy);letter-spacing:-0.2px}
  .content p{font-size:11.2px;line-height:14.5px;font-weight:500}
  .offers{list-style:none;margin-top:5px}
  .offers li{position:relative;padding-left:18px;font-size:11.2px;line-height:14.5px;font-weight:500;margin-bottom:5.5px}
  .offers li svg{position:absolute;left:0;top:2px}
  .block{margin-top:11px}
  .block h2{margin-bottom:1px}
  .partner{margin-top:12px}
  .contact{margin-top:10px;font-size:11.2px;font-weight:500;line-height:20px}
  .contact span{display:inline-block;width:51px}
  .cta{position:absolute;left:293px;top:486px;width:108px;height:88px;z-index:2}
  .cta svg{position:absolute;left:0;top:0}
  .cta__text{position:relative;display:block;color:#fff;font-weight:800;font-size:11.5px;line-height:15.5px;text-align:center;padding-top:13px}
</style>
</head>
<body>

<section class="page page--front">
  <svg class="art" width="465" height="656" viewBox="0 0 465 656">
    <defs>
      <linearGradient id="photoTone" x1="0" y1="0" x2="0.4" y2="1">
        <stop offset="0" stop-color="#6f7848"/>
        <stop offset="0.35" stop-color="#b89a7c"/>
        <stop offset="0.7" stop-color="#8f9cb8"/>
        <stop offset="1" stop-color="#4c6185"/>
      </linearGradient>
    </defs>
    <rect width="465" height="600" fill="url(#photoTone)" role="img" aria-label="Foto: drei lachende Senioren im Sommerurlaub in der Natur"/>
    <path d="M0,576 C150,582 350,545 465,488 L465,656 L0,656 Z" fill="#ffffff"/>
    <path d="M190,398 C205,352 300,346 380,352 C432,356 452,405 440,470 C428,540 398,574 330,571 C250,568 172,540 172,470 C172,440 180,420 190,398 Z" fill="#1f2545"/>
  </svg>
  <div class="headline headline__main">Urlaub</div>
  <div class="headline headline__accent">mit Pflege</div>
  <div class="headline__rule"></div>
  <div class="headline headline__sub">sicher &amp; begleitet<br>reisen</div>
  <div class="badge">Neu<br><span>ab Herbst<br>2025</span></div>
  <div class="footer">
    <div class="brand"><div class="brand__dot"></div><div class="brand__name">Sonnenweg Touren</div></div>
    <div class="footer__url">www.sonnenweg-touren.de</div>
  </div>
</section>

<section class="page page--back">
  <svg class="art" width="465" height="656" viewBox="0 0 465 656">
    <path d="M0,576 C150,582 350,545 465,488 L465,656 L0,656 Z" fill="#ffffff"/>
  </svg>
  <div class="content">
    <h2>Was wir bieten</h2>
    <ul class="offers">
      <li><svg width="11" height="10" viewBox="0 0 11 10"><path d="M1,5.5 L4,8.5 L10,1" fill="none" stroke="#e8782c" stroke-width="2.2" stroke-linecap="round" stroke-linejoin="round"/></svg>Begleitung durch erfahrene Pflegefachkräfte</li>
      <li><svg width="11" height="10" viewBox="0 0 11 10"><path d="M1,5.5 L4,8.5 L10,1" fill="none" stroke="#e8782c" stroke-width="2.2" stroke-linecap="round" stroke-linejoin="round"/></svg>Körperpflege, Medikamentengabe &amp; Betreuung wie zuhause</li>
      <li><svg width="11" height="10" viewBox="0 0 11 10"><path d="M1,5.5 L4,8.5 L10,1" fill="none" stroke="#e8782c" stroke-width="2.2" stroke-linecap="round" stroke-linejoin="round"/></svg>24-Stunden-Erreichbarkeit unserer Pflegekräfte vor Ort im<br>gebuchten Hotel</li>
      <li><svg width="11" height="10" viewBox="0 0 11 10"><path d="M1,5.5 L4,8.5 L10,1" fill="none" stroke="#e8782c" stroke-width="2.2" stroke-linecap="round" stroke-linejoin="round"/></svg>Zusammenarbeit mit ausgewählten Hotels – barrierefrei &amp;<br>seniorengerecht</li>
      <li><svg width="11" height="10" viewBox="0 0 11 10"><path d="M1,5.5 L4,8.5 L10,1" fill="none" stroke="#e8782c" stroke-width="2.2" stroke-linecap="round" stroke-linejoin="round"/></svg>Kleine Gruppen &amp; individuelle Betreuung vor Ort</li>
    </ul>
    <div class="block">
      <h2>Gut zu wissen</h2>
      <p>Für unsere pflegerische Begleitung entstehen Ihnen keine zusätzlichen Kosten, wenn Sie einen Pflegegrad haben und das Verhinderungspflege-Budget noch nicht aufgebraucht ist. Lediglich die Hotelkosten sind von Ihnen selbst zu tragen.</p>
    </div>
    <div class="block">
      <h2>Wer hat Anspruch auf Verhinderungspflege?</h2>
      <p>Alle Pflegebedürftigen mit einem anerkannten Pflegegrad ab Stufe 2 können jährlich Verhinderungspflege über die Pflegekasse abrufen – ideal, um sich im Urlaub sicher begleiten zu lassen!</p>
    </div>
    <div class="block">
      <h2>Unser Service – Ihr Mehrwert</h2>
      <p>Wir organisieren Ihre Reise von A bis Z und begleiten Sie oder Ihre Angehörigen auf dem Weg zu Erholung und neuen Eindrücken – mit Herz, Kompetenz und Erfahrung. Vor Ort sind müssen Sie auf nichts verzichten und werden versorgt wie zu Hause. Gerne organisieren wir auch die Abholung aus ihrer Häuslichkeit.</p>
    </div>
    <div class="partner">
      <h2>Sonnenweg Touren – Ihr verlässlicher<br>Partner für Pflege und Lebensfreude</h2>
      <div class="contact">
        <div><span>Telefon:</span>0381 - 72946183</div>
        <div><span>E-Mail:</span>Mail@sonnenweg-touren .de</div>
      </div>
    </div>
  </div>
  <div class="cta">
    <svg width="108" height="88" viewBox="0 0 108 88"><path d="M20,8 C45,-4 90,0 103,28 C112,52 98,84 62,87 C28,90 2,72 1,48 C0,30 6,15 20,8 Z" fill="#e8782c"/></svg>
    <span class="cta__text">Jetzt<br>informieren<br>&amp; Platz<br>sichern!</span>
  </div>
  <div class="footer">
    <div class="brand"><div class="brand__dot"></div><div class="brand__name">Sonnenweg Touren</div></div>
    <div class="footer__url">www.sonnenweg-touren.de</div>
  </div>
</section>

</body>
</html>
```